Design of labels for exciting new natural skincare products...natural deodorant

I need some labels designed for a range of natural skincare, initially a natural deodorant paste. i will be offering a range of fragrances so i want a basic idea that i can drop different colours / ingredients into easily.

Fragrances are:
1. Jasmine, Orange and Bergamot
2. Lavender & Bergamot
3. Peppermint & Tea tree
4. Unscented
5. Lime, Lemongrass & Ginger

I am a new startup and will be selling online and through a couple of specialty online stores. The final design should encompass our ethos which is clean and green, not fussy nor clinical but friendly and easily accessible. I like fresh, contemporary modern look referencing vintage aesthetics.

The idea is that these products are better for your body AND the environment, and we pledge to use no plastic to package or distribute our products. i like the use of contemporary pastels such as soft pinks, tans and green/blue/aquas, though am open to new ideas too. the logo (attached) appears in red but that should not necessarily be used. i also like black and white with touches of colour.

Target Market(s)

Eco aware, health concious consumers with a reasonable skincare budget.

Industry/Entity Type

Skin Care Product

Font styles to use
Serif
Sans Serif
Decorative

Colors
2eb6a2
b768aa
eea4c8
fabb94
85cae6
cfeae6
eaf2ce
000000
eaeaea

Requirements
Must have
• Labels are for a small glass jar - the dimensions are 2cm high only and wrapping around the jar - at least 10cm wide. i'm also going to be providing a smaller size so this needs to be able to scale down to 1.5cm high and 8cm wide.
• the logo (supplied)
• title: Natural Deodorant
• Subtitle: Orange, Jasmine & Bergamot
• 45g
• Ingredients: tapioca starch*, bicarbonate of soda, Coconut oil*, shea butter*, mango butter*, diatomaceous earth*, sweet almond oil*, vitamin e*, tea tree oil*, Sweet orange essential oil*, Jasmine essential oil*, Bergamot essential oil*.
• *Certified organic ingredient
• (DESIGNERS - PLEASE NOTE NOT ALL THE INGREDIENTS ARE ORGANIC, PLEASE LIST THEM WITH A STAR * IF I HAVE SUPPLIED IT, THEN *Certified organic ingredient BELOW IN SLIGHTLY SMALLER TEXT - THIS SERVES AS THE KEY FOR THE INGREDIENTS LIST)
• pebblewick.nz
• Massage a pea-sized amount onto clean, dry armpits for an odour-free day.
• If irritation develops discontinue use and contact Fern Hollow. (please italicise the company name)
Nice to have
• open to ideas - i am attaching some examples of designs i like, you'll notice i swing between plain black and white aesthetics and a more decorative look. In general i like the old "medicine bottle" look, with hand sketched illustrations. But i'm open to ideas!

```html
<!DOCTYPE html>
<html lang="en">
<head>
<meta charset="utf-8">
<title>Fern Hollow Natural Deodorant Labels</title>
<link rel="stylesheet" href="https://fonts.googleapis.com/css2?family=Oswald:wght@500;600&family=Old+Standard+TT:wght@400;700&family=Open+Sans:ital,wght@0,400;0,600;1,400&display=swap">
<style>
  :root {
    --paper: #ffffff;
    --kraft: #c9a57d;
    --kraft-edge: #b8936b;
    --ink: #2a1c14;
    --ink-soft: #5a4534;
    --band-teal: #2a8fae;
    --band-sky: #8fcde2;
    --band-sun: #f6c62a;
    --band-tangerine: #f47c2c;
  }
  * { box-sizing: border-box; margin: 0; padding: 0; }
  html, body { width: 1200px; height: 1059px; overflow: hidden; background: var(--paper); }
  .sheet {
    width: 1200px; height: 1059px;
    display: grid;
    grid-template-columns: 1fr 1fr;
    grid-template-rows: 1fr 1fr;
    place-items: center;
  }
  .label {
    position: relative;
    width: 540px; height: 190px;
    background: var(--kraft);
    border-top: 1px solid var(--kraft-edge);
    border-bottom: 1px solid var(--kraft-edge);
    color: var(--ink);
    font-family: "Open Sans", sans-serif;
    display: grid;
    grid-template-columns: 160px 210px 44px 1fr;
    column-gap: 12px;
    padding: 0 0 0 14px;
    overflow: hidden;
  }
  .label__info, .label__side {
    font-size: 7px; line-height: 1.35; color: var(--ink-soft);
    padding-top: 16px;
    display: flex; flex-direction: column; gap: 6px;
  }
  .label__info em, .label__side em { font-style: italic; }
  .label__badges { display: flex; gap: 8px; margin-top: 4px; }
  .badge { width: 20px; height: 14px; border-radius: 50%; background: var(--ink-soft); opacity: .55; }
  .label__title {
    display: flex; flex-direction: column; align-items: flex-end; justify-content: center;
  }
  .title__kicker {
    font-family: "Old Standard TT", serif; font-size: 14px; letter-spacing: 3px;
  }
  .title__main {
    font-family: "Oswald", sans-serif; font-weight: 600;
    font-size: 44px; line-height: 1; letter-spacing: 1px;
    padding-bottom: 4px;
    border-bottom: 1.5px solid var(--ink);
  }
  .title__meta {
    display: flex; align-items: stretch; align-self: stretch; margin-top: 4px;
  }
  .title__weight {
    font-family: "Old Standard TT", serif; font-size: 30px; line-height: 1;
    padding-right: 8px; border-right: 1.5px solid var(--ink);
  }
  .title__scent {
    font-family: "Old Standard TT", serif; font-size: 13px; letter-spacing: 1.5px; line-height: 1.15;
    padding-left: 10px; align-self: center;
  }
  .label__band {
    display: flex; align-items: center; justify-content: center;
    height: 120px; align-self: center;
  }
  .band__name {
    writing-mode: vertical-rl; transform: rotate(180deg);
    font-family: "Old Standard TT", serif; font-weight: 700; font-size: 15px;
    color: var(--kraft);
  }
  .label--teal .label__band { background: var(--band-teal); }
  .label--sky .label__band { background: var(--band-sky); }
  .label--sun .label__band { background: var(--band-sun); }
  .label--tangerine .label__band { background: var(--band-tangerine); }
</style>
</head>
<body>
<main class="sheet">
  <section class="label label--teal" aria-label="Lavender and Bergamot label, teal">
    <div class="label__info">
      <p>Massage a pea-sized amount onto clean, dry armpits for an odour-free day.</p>
      <p>If irritation develops discontinue use and contact <em>Fern Hollow</em>.</p>
      <p>Ingredients: Coconut oil*, tapioca starch*, bicarbonate of soda, mango butter*, shea butter*, diatomaceous earth*, sweet almond oil*, tea tree oil*, Sweet orange essential oil*, Jasmine essential oil*, Bergamot essential oil*</p>
      <div class="label__badges"><span class="badge"></span><span class="badge"></span></div>
    </div>
    <div class="label__title">
      <span class="title__kicker">NATURAL</span>
      <h2 class="title__main">DEODORANT</h2>
      <div class="title__meta"><span class="title__weight">50g</span><span class="title__scent">LAVENDER &amp;<br>BERGAMOT</span></div>
    </div>
    <div class="label__band"><span class="band__name">Fern Hollow</span></div>
    <div class="label__side">
      <p>Massage a pea-sized amount onto clean, dry armpits for an odour-free day.</p>
      <p>If irritation develops discontinue use and contact <em>Fern Hollow</em>.</p>
    </div>
  </section>

  <section class="label label--sky" aria-label="Lavender and Bergamot label, sky blue">
    <div class="label__info">
      <p>Massage a pea-sized amount onto clean, dry armpits for an odour-free day.</p>
      <p>If irritation develops discontinue use and contact <em>Fern Hollow</em>.</p>
      <p>Ingredients: Coconut oil*, tapioca starch*, bicarbonate of soda, mango butter*, shea butter*, diatomaceous earth*, sweet almond oil*, tea tree oil*, Sweet orange essential oil*, Jasmine essential oil*, Bergamot essential oil*</p>
      <div class="label__badges"><span class="badge"></span><span class="badge"></span></div>
    </div>
    <div class="label__title">
      <span class="title__kicker">NATURAL</span>
      <h2 class="title__main">DEODORANT</h2>
      <div class="title__meta"><span class="title__weight">50g</span><span class="title__scent">LAVENDER &amp;<br>BERGAMOT</span></div>
    </div>
    <div class="label__band"><span class="band__name">Fern Hollow</span></div>
    <div class="label__side">
      <p>Massage a pea-sized amount onto clean, dry armpits for an odour-free day.</p>
      <p>If irritation develops discontinue use and contact <em>Fern Hollow</em>.</p>
    </div>
  </section>

  <section class="label label--sun" aria-label="Lavender and Bergamot label, yellow">
    <div class="label__info">
      <p>Massage a pea-sized amount onto clean, dry armpits for an odour-free day.</p>
      <p>If irritation develops discontinue use and contact <em>Fern Hollow</em>.</p>
      <p>Ingredients: Coconut oil*, tapioca starch*, bicarbonate of soda, mango butter*, shea butter*, diatomaceous earth*, sweet almond oil*, tea tree oil*, Sweet orange essential oil*, Jasmine essential oil*, Bergamot essential oil*</p>
      <div class="label__badges"><span class="badge"></span><span class="badge"></span></div>
    </div>
    <div class="label__title">
      <span class="title__kicker">NATURAL</span>
      <h2 class="title__main">DEODORANT</h2>
      <div class="title__meta"><span class="title__weight">50g</span><span class="title__scent">LAVENDER &amp;<br>BERGAMOT</span></div>
    </div>
    <div class="label__band"><span class="band__name">Fern Hollow</span></div>
    <div class="label__side">
      <p>Massage a pea-sized amount onto clean, dry armpits for an odour-free day.</p>
      <p>If irritation develops discontinue use and contact <em>Fern Hollow</em>.</p>
    </div>
  </section>

  <section class="label label--tangerine" aria-label="Lavender and Bergamot label, orange">
    <div class="label__info">
      <p>Massage a pea-sized amount onto clean, dry armpits for an odour-free day.</p>
      <p>If irritation develops discontinue use and contact <em>Fern Hollow</em>.</p>
      <p>Ingredients: Coconut oil*, tapioca starch*, bicarbonate of soda, mango butter*, shea butter*, diatomaceous earth*, sweet almond oil*, tea tree oil*, Sweet orange essential oil*, Jasmine essential oil*, Bergamot essential oil*</p>
      <div class="label__badges"><span class="badge"></span><span class="badge"></span></div>
    </div>
    <div class="label__title">
      <span class="title__kicker">NATURAL</span>
      <h2 class="title__main">DEODORANT</h2>
      <div class="title__meta"><span class="title__weight">50g</span><span class="title__scent">LAVENDER &amp;<br>BERGAMOT</span></div>
    </div>
    <div class="label__band"><span class="band__name">Fern Hollow</span></div>
    <div class="label__side">
      <p>Massage a pea-sized amount onto clean, dry armpits for an odour-free day.</p>
      <p>If irritation develops discontinue use and contact <em>Fern Hollow</em>.</p>
    </div>
  </section>
</main>
</body>
</html>
```